Business Card Design Project

Design is for the business card of a holistic, integral therapist. Design is required for front (colour / pattern) and back (white, with text as below).

Please prepare the design using placeholder text. I will work with the winning submission to complete the final information in the last iteration.

To give you a sense of her services a profile is below:
- I offer an integrative approach for effective relief of many issues such as anxiety, panic attacks, relationship difficulties, and health problems. In my counselling sessions I mainly use QBR {Quiet Balance Release } which taps into the body's energy system (meridians) to clear up blockages and limiting /distorted thinking and beliefs. I also work on expanding awareness as well as enhancing relationships.Clients have found the sessions life changing and report feeling lighter, clearer more empowered and connected to themselves and others.

Target Market(s)

Well educated, upper socioeconomic people seeking purpose and happiness in their lives.

Industry/Entity Type

Health

Requirements
Must have
• Must have the following text on front

First Name, Last Name
LLB, ND, Dip C
Counselling & Naturopathy
Quiet Balnce Release and Marlow Therapy

Adress 1 Line 1
Adress 1 Line 2

Adress 2 Line 1
Adress 2 Line 2

xxx.xxx@xxxxx.com

Tel: 0XXX XXX XXX

Must have the following text on reverse - which should be primarily white.

Next appointment
Date:
Time:
Nice to have
• Example colour palettes

http://www.huebinder.example/swatch/512093/velvet_lantern
http://www.huebinder.example/swatch/318420/Quiet_Orchard
http://www.huebinder.example/swatch/607215/Morning_Over_Tides

Example images that may be useful...
http://www.shopvarn.example/gp/product/images/4719205536/ref=dp_image_text_0?ie=UTF8&n=517302&s=books
http://www.shopvarn.example/gp/customer-media/product-gallery/6284019573/ref=cm_ciu_pdp_images_all
http://en.loreweb.example/wiki/File:Lotus_Grid_256bw.gif

```html
<!DOCTYPE html>
<html lang="en">
<head>
<meta charset="utf-8">
<title>Therapist Business Card – Front and Reverse</title>
<link rel="stylesheet" href="https://fonts.googleapis.com/css2?family=Fira+Sans:wght@300;400;500&display=swap">
<style>
  :root {
    --page-bg: #fbfde6;
    --card-dark: #45382c;
    --card-light: #ffffff;
    --ink-dark: #3a2f26;
    --name-lime: #c9e04b;
    --text-cream: #f3f0b8;
    --address-green: #86d35f;
    --icon-yellow: #e6e44a;
    --motif-green: #7fbf6a;
    --motif-yellow: #dfe48a;
  }
  * { box-sizing: border-box; margin: 0; padding: 0; }
  html, body {
    width: 1200px; height: 900px; overflow: hidden;
    background: var(--page-bg);
    font-family: "Fira Sans", sans-serif;
  }
  .stage { position: relative; width: 1200px; height: 900px; }

  .card {
    position: absolute;
    width: 700px; height: 420px;
    border-radius: 26px;
  }
  .card--reverse {
    left: 440px; top: 50px;
    background: var(--card-light);
    box-shadow: 0 4px 14px rgba(60, 50, 30, 0.12);
  }
  .card--front {
    left: 70px; top: 410px;
    background: var(--card-dark);
    box-shadow: 0 6px 18px rgba(40, 30, 20, 0.3);
  }

  .yantra {
    position: absolute;
    width: 290px; height: 290px;
    background: linear-gradient(160deg, var(--motif-green), var(--motif-yellow));
  }
  .card--reverse .yantra { right: 50px; top: 62px; }
  .card--front .yantra { right: 45px; top: 58px; }

  .appointment { position: absolute; left: 56px; top: 122px; color: var(--ink-dark); }
  .appointment__title { font-size: 26px; font-weight: 400; margin-bottom: 22px; }
  .appointment__field { font-size: 14px; font-weight: 400; margin-left: 32px; margin-bottom: 16px; }

  .details { position: absolute; left: 42px; top: 96px; width: 330px; }
  .details__name {
    font-size: 26px; font-weight: 400; color: var(--name-lime);
    line-height: 1.2; margin-bottom: 6px;
  }
  .details__credentials {
    list-style: none; margin-left: 40px; margin-bottom: 18px;
    font-size: 14px; font-weight: 300; line-height: 18px; color: var(--text-cream);
  }
  .address {
    font-size: 14px; font-weight: 300; line-height: 19px; color: var(--address-green);
    margin-left: 30px; margin-bottom: 14px; font-style: normal;
  }
  .address--second { margin-left: 34px; margin-bottom: 12px; }
  .contact { list-style: none; margin-left: 72px; }
  .contact__item {
    display: flex; align-items: center; gap: 10px;
    font-size: 14px; font-weight: 300; line-height: 18px; color: var(--text-cream);
  }
  .contact__icon { width: 15px; height: 13px; flex: none; }
</style>
</head>
<body>
<main class="stage">

  <section class="card card--reverse" aria-label="Card reverse">
    <div class="appointment">
      <h2 class="appointment__title">Next appointment</h2>
      <p class="appointment__field">Date</p>
      <p class="appointment__field">Time</p>
    </div>
    <div class="yantra" role="img" aria-label="Sacred geometry yantra motif in green, yellow and orange"></div>
  </section>

  <section class="card card--front" aria-label="Card front">
    <div class="details">
      <h1 class="details__name">First Last Name</h1>
      <ul class="details__credentials">
        <li>LLB | ND | Dip C</li>
        <li>Counselling &amp; Naturopathy</li>
        <li>Quiet Balance Release</li>
        <li>Marlow Therapy</li>
      </ul>
      <address class="address">1 Building, 1234 Street Name<br>City 1, Country</address>
      <address class="address address--second">2 Building, 5678 Street Name<br>City 2, Country</address>
      <ul class="contact">
        <li class="contact__item">
          <svg class="contact__icon" viewBox="0 0 16 14" aria-hidden="true">
            <rect x="1" y="2" width="14" height="10" fill="none" stroke="var(--icon-yellow)" stroke-width="1.8"/>
            <path d="M1 2 L8 8 L15 2" fill="none" stroke="var(--icon-yellow)" stroke-width="1.6"/>
          </svg>
          first.last@stillwater.example
        </li>
        <li class="contact__item">
          <svg class="contact__icon" viewBox="0 0 16 14" aria-hidden="true">
            <path d="M2 3 Q2 1 4 1 L12 1 Q14 1 14 3 L12 5 L10 3 L6 3 L4 5 Z" fill="var(--icon-yellow)"/>
            <rect x="3" y="6" width="10" height="7" rx="1.5" fill="var(--icon-yellow)"/>
          </svg>
          0100.555.010
        </li>
      </ul>
    </div>
    <div class="yantra" role="img" aria-label="Sacred geometry yantra motif in green, yellow and orange"></div>
  </section>

</main>
</body>
</html>
```